Aviation Banner Ad Designs

SkyLedgerMetrics provides access to the most accurate aircraft operating cost information, to compare Piston, Turboprop and Jet aircraft.

The banners ads will be used for retargeting/remarketing - to bring visitors back to the site. The banners should remind and reinforce the key messages of what the site provides.

Target Market(s)

Private aircraft buyers including:
- Aircraft Brokers
- Charter Operators
- Corporate Flight Departments
- Aircraft Management companies
- Financial Institutions
- Aircraft Owners
- Prospective Buyers

Requirements
Must have
• A. Banner Objective
The visual and textual content of the banner should remind the viewer about the features of the site, and prompt them to return to the site.
1. Arresting visual
2. Headline
3. Single message
4. Compelling CTA
5. Logo - big enough to see
6. Standard IAB ad sizes/specs

B. Design Elements
Logo: As attached
Main Title: Calculate Jet Operating Costs
Subtitle: Compare Ownership Usage Scenarios
Call to Action Button: Compare Ownership Costs
Background: Several images supplied as options

C. Banner Sizes
Do examples as 300×250 , 728×90 , 160×600
Final sizes to also include 320×100 , 336x280 , 300x600

Finally delivery as .jpg files.

Font - use same font as on site

```html
<!DOCTYPE html>
<html lang="en">
<head>
<meta charset="utf-8">
<title>SkyLedgerMetrics – Banner Set</title>
<link rel="stylesheet" href="https://fonts.googleapis.com/css2?family=Bebas+Neue&family=Lato:wght@700;900&display=swap">
<style>
  :root {
    --stage: #000000;
    --paper: #ffffff;
    --headline: #1f67a3;
    --ink: #111111;
    --cta: #45b649;
    --cta-text: #ffffff;
    --rim: #e2e2e2;
    --sky-haze: #f2f2f2;
    --sky-cloud: #c9cbcf;
    --sky-slate: #9ea4ab;
    --sky-amber: #d48d55;
    --sky-glow: #f3c690;
    --sky-dusk: #8f6a55;
  }
  * { box-sizing: border-box; margin: 0; padding: 0; }
  html, body {
    width: 1200px; height: 625px; overflow: hidden;
    background: var(--stage);
  }
  .stage {
    position: relative; width: 1302px; height: 678px;
    transform: scale(0.9217); transform-origin: 0 0;
  }
  .banner {
    position: absolute; background: var(--paper); overflow: hidden;
    font-family: "Lato", Arial, sans-serif;
  }
  .sky {
    position: absolute; left: 0; top: 0;
    background:
      radial-gradient(ellipse 55% 38% at 12% 92%, var(--sky-dusk) 0%, rgba(143,106,85,0) 100%),
      radial-gradient(ellipse 70% 45% at 30% 100%, var(--sky-amber) 0%, rgba(212,141,85,0) 100%),
      radial-gradient(ellipse 60% 35% at 80% 96%, var(--sky-glow) 0%, rgba(243,198,144,0) 100%),
      radial-gradient(ellipse 80% 30% at 60% 55%, var(--sky-slate) 0%, rgba(158,164,171,0) 100%),
      linear-gradient(180deg, var(--paper) 0%, var(--sky-haze) 16%, var(--sky-cloud) 45%, #c7b09a 78%, var(--sky-glow) 100%);
    box-shadow: 0 3px 0 var(--rim);
  }
  .sky--bottom { border-radius: 0 0 50% 50% / 0 0 22px 22px; }
  .sky--side {
    border-radius: 0 30px 30px 0 / 0 50% 50% 0;
    box-shadow: 3px 0 0 var(--rim);
  }
  .sky--faded::before {
    content: ""; position: absolute; inset: 0;
    background: linear-gradient(90deg, var(--paper) 0%, rgba(255,255,255,0) 30%);
  }
  .brand {
    position: absolute; left: 0; width: 100%;
    display: flex; align-items: center; justify-content: center; gap: 6px;
    font-family: "Lato", Arial, sans-serif; font-weight: 900;
    color: var(--ink); white-space: nowrap; line-height: 1;
  }
  .brand__mark { display: block; flex: none; background: var(--cta); }
  .headline {
    position: absolute; left: 0; width: 100%; text-align: center;
    font-family: "Bebas Neue", "Oswald", sans-serif; font-weight: 400;
    color: var(--headline); line-height: 1; letter-spacing: 0.3px;
  }
  .subline {
    position: absolute; left: 0; width: 100%; text-align: center;
    font-weight: 900; color: var(--ink); text-transform: uppercase; line-height: 1.2;
  }
  .cta {
    position: absolute; display: flex; align-items: center; justify-content: center; gap: 8px;
    background: var(--cta); color: var(--cta-text); border-radius: 2px;
    font-weight: 900; text-transform: uppercase; white-space: nowrap;
  }
  .cta svg { flex: none; }
</style>
</head>
<body>
<div class="stage">

  <!-- 300 x 250 -->
  <section class="banner" style="left:24px;top:41px;width:300px;height:250px">
    <div class="sky sky--bottom" style="width:300px;height:146px" role="img" aria-label="Business jet climbing through a sunset sky with warm clouds"></div>
    <div class="brand" style="top:17px;font-size:15px"><span class="brand__mark" style="width:16px;height:16px"></span>SkyLedgerMetrics</div>
    <h2 class="headline" style="top:166px;font-size:18px">Calculate Jet Operating Costs</h2>
    <p class="subline" style="top:186px;font-size:8.5px">Compare Ownership Usage Scenarios</p>
    <a class="cta" style="left:68px;top:206px;width:160px;height:28px;font-size:8px">Compare Ownership Costs
      <svg width="6" height="10" viewBox="0 0 6 10"><path d="M1 1l4 4-4 4" fill="none" stroke="#fff" stroke-width="1.6"/></svg></a>
  </section>

  <!-- 336 x 280 -->
  <section class="banner" style="left:416px;top:44px;width:336px;height:280px">
    <div class="sky sky--bottom" style="width:336px;height:152px" role="img" aria-label="Business jet climbing through a sunset sky with warm clouds"></div>
    <div class="brand" style="top:17px;font-size:15px"><span class="brand__mark" style="width:16px;height:16px"></span>SkyLedgerMetrics</div>
    <h2 class="headline" style="top:175px;font-size:20px">Calculate Jet Operating Costs</h2>
    <p class="subline" style="top:196px;font-size:9px">Compare Ownership Usage Scenarios</p>
    <a class="cta" style="left:65px;top:222px;width:183px;height:29px;font-size:8.5px">Compare Ownership Costs
      <svg width="6" height="10" viewBox="0 0 6 10"><path d="M1 1l4 4-4 4" fill="none" stroke="#fff" stroke-width="1.6"/></svg></a>
  </section>

  <!-- 320 x 100 -->
  <section class="banner" style="left:24px;top:324px;width:320px;height:100px">
    <div class="sky sky--side" style="width:125px;height:100px" role="img" aria-label="Business jet climbing through a sunset sky with warm clouds"></div>
    <div class="brand" style="left:125px;width:195px;top:12px;font-size:13px"><span class="brand__mark" style="width:14px;height:14px"></span>SkyLedgerMetrics</div>
    <h2 class="headline" style="left:125px;width:195px;top:41px;font-size:14px">Calculate Jet Operating Costs</h2>
    <p class="subline" style="left:125px;width:195px;top:57px;font-size:7.5px">Compare Ownership Usage Scenarios</p>
    <a class="cta" style="left:147px;top:71px;width:153px;height:19px;font-size:7.5px;gap:6px">Compare Ownership Costs
      <svg width="5" height="8" viewBox="0 0 6 10"><path d="M1 1l4 4-4 4" fill="none" stroke="#fff" stroke-width="1.8"/></svg></a>
  </section>

  <!-- 728 x 90 -->
  <section class="banner" style="left:24px;top:551px;width:728px;height:90px">
    <div class="sky sky--side sky--faded" style="left:145px;width:253px;height:90px;border-radius:0 40px 40px 0 / 0 50% 50% 0" role="img" aria-label="Business jet climbing through a sunset sky with warm clouds"></div>
    <div class="brand" style="left:20px;width:auto;top:37px;font-size:15px"><span class="brand__mark" style="width:16px;height:16px"></span>SkyLedgerMetrics</div>
    <h2 class="headline" style="left:400px;width:314px;top:11px;font-size:23px">Calculate Jet Operating Costs</h2>
    <p class="subline" style="left:400px;width:314px;top:34px;font-size:9.5px">Compare Ownership Usage Scenarios</p>
    <a class="cta" style="left:479px;top:52px;width:183px;height:29px;font-size:8.5px">Compare Ownership Costs
      <svg width="6" height="10" viewBox="0 0 6 10"><path d="M1 1l4 4-4 4" fill="none" stroke="#fff" stroke-width="1.6"/></svg></a>
  </section>

  <!-- 160 x 600 -->
  <section class="banner" style="left:779px;top:41px;width:160px;height:600px">
    <div class="sky sky--bottom" style="width:160px;height:278px" role="img" aria-label="Business jet climbing through a sunset sky with warm clouds"></div>
    <div class="brand" style="top:32px;font-size:13px;gap:5px"><span class="brand__mark" style="width:14px;height:14px"></span>SkyLedgerMetrics</div>
    <h2 class="headline" style="top:382px;font-size:24px;line-height:1.02">Calculate Jet<br>Operating Costs</h2>
    <p class="subline" style="top:436px;font-size:9px">Compare Ownership<br>Usage Scenarios</p>
    <a class="cta" style="left:5px;top:535px;width:150px;height:28px;font-size:7.5px;gap:6px">Compare Ownership Costs
      <svg width="6" height="10" viewBox="0 0 6 10"><path d="M1 1l4 4-4 4" fill="none" stroke="#fff" stroke-width="1.6"/></svg></a>
  </section>

  <!-- 300 x 600 -->
  <section class="banner" style="left:957px;top:41px;width:300px;height:600px">
    <div class="sky sky--bottom" style="width:300px;height:298px" role="img" aria-label="Business jet climbing through a sunset sky with warm clouds"></div>
    <div class="brand" style="top:37px;font-size:18px;gap:8px"><span class="brand__mark" style="width:19px;height:19px"></span>SkyLedgerMetrics</div>
    <h2 class="headline" style="top:396px;font-size:30px;line-height:1.02">Calculate Jet<br>Operating Costs</h2>
    <p class="subline" style="top:465px;font-size:11px">Compare Ownership<br>Usage Scenarios</p>
    <a class="cta" style="left:59px;top:536px;width:183px;height:29px;font-size:8.5px">Compare Ownership Costs
      <svg width="6" height="10" viewBox="0 0 6 10"><path d="M1 1l4 4-4 4" fill="none" stroke="#fff" stroke-width="1.6"/></svg></a>
  </section>

</div>
</body>
</html>
```